Letterhead to Prospective Clients

Create a letterhead (word & canva) that I will use to send letters to prospective clients and also include the Coralwood Estate Partners Logo, My Contact Details and Interchangeable "Suburb". Use the same font and colour pallete

Maris Dulworth | "Suburb" Specialist - Redlands & Surrounds
Mobile: 0417 862 095
Email: MD@CoralwoodEstatePartners.com.au

```html
<!DOCTYPE html>
<html lang="en">
<head>
<meta charset="utf-8">
<title>Coralwood Estate Partners Letterhead</title>
<link href="https://fonts.googleapis.com/css2?family=Arimo:wght@400;700&family=Crimson+Pro:ital,wght@1,400&display=swap" rel="stylesheet">
<style>
  :root {
    --navy: #0b1a3a;
    --paper: #fdf8f4;
    --ink: #222222;
    --sig: #e9e2da;
  }
  html, body {
    margin: 0;
    padding: 0;
    width: 1200px;
    height: 1000px;
    overflow: hidden;
    background: var(--navy);
  }
  .canvas {
    position: relative;
    width: 1200px;
    height: 1000px;
  }
  .letter {
    position: absolute;
    left: 266px;
    top: 27px;
    width: 668px;
    height: 945px;
    background: var(--paper);
    font-family: "Arimo", Arial, sans-serif;
    color: var(--ink);
  }
  .letter > * { position: absolute; margin: 0; }
  .brand-name {
    left: 66px;
    top: 66px;
    width: 330px;
    font-size: 23px;
    font-weight: 400;
    letter-spacing: 1px;
    color: var(--navy);
    line-height: 1;
    white-space: nowrap;
  }
  .top-rule {
    left: 421px;
    top: 92px;
    width: 182px;
    height: 4px;
    background: var(--navy);
  }
  .side-rule {
    left: 598px;
    top: 696px;
    width: 4px;
    height: 182px;
    background: var(--navy);
  }
  .agent-line {
    left: 66px;
    top: 225px;
    font-family: "Crimson Pro", Georgia, serif;
    font-style: italic;
    font-size: 14px;
    white-space: nowrap;
  }
  .date {
    left: 66px;
    top: 281px;
    font-size: 13.5px;
    font-weight: 700;
  }
  .salutation {
    left: 66px;
    top: 335px;
    font-size: 13.5px;
  }
  .body-copy {
    left: 66px;
    top: 367px;
    width: 489px;
    font-size: 13.3px;
    line-height: 18px;
    text-align: justify;
  }
  .body-copy p { margin: 0 0 22px; }
  .closing {
    left: 66px;
    top: 613px;
    font-size: 13.5px;
  }
  .signature {
    left: 54px;
    top: 668px;
    width: 246px;
    height: 62px;
    background: linear-gradient(90deg, var(--sig), var(--paper));
  }
  .sign-off {
    left: 66px;
    top: 743px;
    font-size: 13.5px;
    font-weight: 700;
  }
  .contact {
    left: 66px;
    top: 838px;
    width: 489px;
    text-align: right;
    font-size: 13.3px;
    font-weight: 700;
    color: var(--navy);
    line-height: 21px;
  }
</style>
</head>
<body>
<div class="canvas">
  <article class="letter">
    <div class="brand-name">Coralwood Estate Partners</div>
    <div class="top-rule"></div>

    <p class="agent-line">Maris Dulworth | "Suburb" Specialist - Redlands &amp; Surrounds</p>
    <p class="date">June 24, 2025</p>
    <p class="salutation">Dear,</p>

    <div class="body-copy">
      <p>Lorem ipsum dolor sit amet, consectetur adipiscing elit, sed do eiusmod tempor incididunt ut labore et dolore magna aliqua. Eget nunc lobortis mattis aliquam faucibus purus. Tincidunt praesent semper feugiat nibh. Mi proin sed libero enim sed faucibus turpis. Tempor id eu nisl nunc mi. Suscipit adipiscing bibendum est ultricies integer. Mattis nunc sed blandit libero volutpat sed.</p>
      <p>Ac ut consequat semper viverra nam. Adipiscing bibendum est ultricies integer quis auctor elit sed vulputate. Elit ut aliquam purus sit. Morbi enim nunc faucibus a pellentesque sit amet porttitor. Sem fringilla ut morbi tincidunt augue interdum. Ac turpis egestas sed tempus urna et pharetra. Ullamcorper dignissim cras tincidunt lobortis feugiat vivamus at augue eget.</p>
    </div>

    <p class="closing">Warm regards,</p>
    <div class="signature" role="img" aria-label="Handwritten signature of Tove Lindqvist"></div>
    <p class="sign-off">Best Regards</p>

    <div class="contact">
      <div>Mobile: 0417 862 095</div>
      <div>Email: MD@CoralwoodEstatePartners.com.au</div>
    </div>
    <div class="side-rule"></div>
  </article>
</div>
</body>
</html>
```